Funky Cup design on our hot disposable cups

I would like two examples: one orange cup (like our logo color) with white writing, one white cup with orange writing:
On the top: Organic coffee because we care
Middle: Our logo (attached but drop the R in the circle)
Bottom: Live Life Like a Tinker
Would love ideas what else can be written or patterned around the cup, clever design such as Coffee moorings or any other funky ideas.

It should include the text "tinkers & tide " all over the cup around the logo!

thanks.

Target Market(s)

female and male 17 to 30s

Industry/Entity Type

Coffee

Font styles to use
Other font styles liked:
• Galano grotesque like our logosame as logo

Colors
EE7325
F08F49
F5BC92
FAE3D3
FDF4ED

Requirements
Must have
• cool fun , trendy look. It should include the text "tinkers & tide " all over the cup around the logo!
Should not have
• in my logo please drop the r with the circle

```html
<!DOCTYPE html>
<html lang="en">
<head>
<meta charset="utf-8">
<title>tinkers &amp; tide — cup designs</title>
<link rel="stylesheet" href="https://fonts.googleapis.com/css2?family=Poppins:wght@500;600;700&display=swap">
<style>
  :root {
    --orange: #EE7325;
    --orange-mid: #F08F49;
    --peach: #F5BC92;
    --blush: #FAE3D3;
    --cream: #FDF4ED;
    --white: #ffffff;
    --stage: #e4e4e4;
    --pattern-on-white: rgba(238, 115, 37, 0.08);
    --pattern-on-orange: rgba(200, 80, 20, 0.28);
  }
  * { margin: 0; padding: 0; box-sizing: border-box; }
  html, body { width: 1200px; height: 900px; overflow: hidden; }
  body {
    background: var(--stage);
    font-family: "Poppins", sans-serif;
    display: flex;
    align-items: center;
    justify-content: center;
    gap: 90px;
  }
  .cup {
    position: relative;
    width: 390px;
    height: 580px;
    clip-path: polygon(0 0, 100% 0, 88% 100%, 12% 100%);
    overflow: hidden;
  }
  .cup--white { background: var(--white); color: var(--orange); }
  .cup--orange { background: linear-gradient(100deg, var(--orange-mid), var(--orange) 70%); color: var(--white); }
  .cup-rim { position: absolute; top: 0; left: 0; right: 0; height: 16px; }
  .cup--white .cup-rim { background: var(--orange); }
  .cup--orange .cup-rim { background: var(--white); }

  .name-pattern {
    position: absolute;
    left: -40px; right: -40px;
    top: 300px;
    display: flex;
    flex-direction: column;
    gap: 4px;
    transform: rotate(-12deg);
    font-weight: 700;
    white-space: nowrap;
    line-height: 1;
  }
  .cup--white .name-pattern { color: var(--pattern-on-white); }
  .cup--orange .name-pattern { color: var(--pattern-on-orange); }
  .name-pattern span:nth-child(1) { font-size: 64px; }
  .name-pattern span:nth-child(2) { font-size: 48px; margin-left: 30px; }
  .name-pattern span:nth-child(3) { font-size: 36px; margin-left: 60px; }
  .name-pattern span:nth-child(4) { font-size: 26px; margin-left: 90px; }
  .name-pattern span:nth-child(5) { font-size: 18px; margin-left: 120px; }

  .cup-message {
    position: absolute;
    top: 70px; left: 0; right: 0;
    transform: rotate(-10deg);
    font-weight: 600;
    font-size: 22px;
    letter-spacing: 0.9em;
    line-height: 1.7;
    text-transform: uppercase;
  }
  .cup-message span { display: block; }
  .cup-message .row-1 { padding-left: 60px; }
  .cup-message .row-2 { padding-left: 80px; }
  .cup-message .row-3 { padding-left: 70px; }
  .cup-message .row-4 { padding-left: 92px; }

  .brand {
    position: absolute;
    top: 290px; left: 0; right: 0;
    display: flex;
    align-items: center;
    justify-content: center;
    gap: 10px;
    transform: rotate(-10deg);
    font-weight: 700;
    font-size: 30px;
  }
  .brand-dot { width: 22px; height: 22px; border-radius: 50%; }
  .cup--white .brand-dot { background: var(--orange); }
  .cup--orange .brand-dot { background: var(--white); }

  .tagline {
    position: absolute;
    top: 370px; left: 0; right: 0;
    text-align: center;
    transform: rotate(-12deg);
    font-weight: 600;
    font-size: 24px;
  }
</style>
</head>
<body>
  <div class="cup cup--white">
    <div class="cup-rim"></div>
    <div class="name-pattern" aria-hidden="true">
      <span>tinkers &amp; tide tinkers</span>
      <span>tinkers &amp; tide tinkers</span>
      <span>tinkers &amp; tide tinkers &amp; tide</span>
      <span>tinkers &amp; tide tinkers &amp; tide</span>
      <span>tinkers &amp; tide tinkers &amp; tide</span>
    </div>
    <p class="cup-message">
      <span class="row-1">Organic</span>
      <span class="row-2">Coffee</span>
      <span class="row-3">Because</span>
      <span class="row-4">We Care</span>
    </p>
    <div class="brand"><span class="brand-dot"></span>tinkers &amp; tide</div>
    <p class="tagline">Live Life Like a Tinker</p>
  </div>

  <div class="cup cup--orange">
    <div class="cup-rim"></div>
    <div class="name-pattern" aria-hidden="true">
      <span>tinkers &amp; tide tinkers</span>
      <span>tinkers &amp; tide tinkers</span>
      <span>tinkers &amp; tide tinkers &amp; tide</span>
      <span>tinkers &amp; tide tinkers &amp; tide</span>
      <span>tinkers &amp; tide tinkers &amp; tide</span>
    </div>
    <p class="cup-message">
      <span class="row-1">Organic</span>
      <span class="row-2">Coffee</span>
      <span class="row-3">Because</span>
      <span class="row-4">We Care</span>
    </p>
    <div class="brand"><span class="brand-dot"></span>tinkers &amp; tide</div>
    <p class="tagline">Live Life Like a Tinker</p>
  </div>
</body>
</html>
```